BRIM Outreach Partners Business Card Rebrand

Hello Designers! We are looking for help designing our new business card to go in conjunction with our company rebrand. Unfortunately, we have an event mid June that requires we get these printed ASAP (before our new website is launched.) We have a mostly complete Brand Book which I have uploaded to this request for your reference to company information, style, fonts. I've also enclosed our logo file in .eps & .jpg. Attached is a sample business card my boss liked but said was "too simple." I made it in Canva and do not profess to be a designer. NOT FOR DESIGN REFERENCE, ONLY FOR CONTEXT Here is what our old website looks like: https://brimoutreachpartners.com/.

```html
<!DOCTYPE html>
<html lang="en">
<head>
<meta charset="UTF-8">
<title>BRIM Outreach Partners Business Card</title>
<link href="https://fonts.googleapis.com/css2?family=Montserrat:wght@300;400;500;700;800&display=swap" rel="stylesheet">
<style>
  :root {
    --ink: #10201f;
    --paper: #ffffff;
    --backdrop: #eeeeee;
    --text-dark: #1b1f1f;
  }
  * { box-sizing: border-box; margin: 0; padding: 0; }
  html, body {
    width: 1200px;
    height: 900px;
    overflow: hidden;
    background: var(--backdrop);
    font-family: "Montserrat", sans-serif;
  }
  .stage {
    width: 1200px;
    height: 900px;
    display: flex;
    align-items: center;
    justify-content: center;
    gap: 40px;
  }
  .card {
    width: 540px;
    height: 309px;
    position: relative;
    overflow: hidden;
    box-shadow: 0 6px 18px rgba(0,0,0,0.12);
  }
  /* Front */
  .card-front {
    background: var(--ink);
    display: flex;
    align-items: center;
    justify-content: center;
  }
  .brand {
    display: flex;
    align-items: center;
    gap: 16px;
    color: var(--paper);
  }
  .brand-dot {
    width: 72px;
    height: 72px;
    border-radius: 50%;
    background: var(--paper);
    flex: none;
  }
  .brand-name {
    font-weight: 700;
    font-size: 26px;
    line-height: 1.1;
    letter-spacing: 0.5px;
    text-transform: uppercase;
  }
  /* Back */
  .card-back {
    background: var(--paper);
    color: var(--text-dark);
  }
  .accent-bar {
    position: absolute;
    left: 30px;
    top: 104px;
    width: 16px;
    height: 44px;
    background: var(--ink);
  }
  .person {
    position: absolute;
    left: 58px;
    top: 104px;
  }
  .person-name {
    font-weight: 800;
    font-size: 19px;
    letter-spacing: 0.3px;
    text-transform: uppercase;
  }
  .person-title {
    font-weight: 300;
    font-size: 11px;
    letter-spacing: 0.6px;
    text-transform: uppercase;
    margin-top: 1px;
  }
  .contact {
    position: absolute;
    left: 30px;
    bottom: 28px;
    list-style: none;
    font-size: 11px;
    font-weight: 400;
    line-height: 1.75;
  }
  .contact-label {
    font-weight: 700;
    display: inline-block;
    width: 20px;
  }
  .gavel-art {
    position: absolute;
    right: 0;
    top: 60px;
    width: 190px;
    height: 195px;
    background: linear-gradient(160deg, #1a2d2c, var(--ink));
  }
  .edge-band {
    position: absolute;
    right: 0;
    bottom: 0;
    width: 100%;
    height: 8px;
    background: var(--ink);
  }
</style>
</head>
<body>
  <main class="stage">
    <section class="card card-front" aria-label="Card front">
      <div class="brand">
        <span class="brand-dot"></span>
        <span class="brand-name">BRIM Outreach<br>Partners</span>
      </div>
    </section>

    <section class="card card-back" aria-label="Card back">
      <span class="accent-bar"></span>
      <div class="person">
        <h1 class="person-name">Daniel Roswell-Hart</h1>
        <p class="person-title">Managing Partner</p>
      </div>
      <ul class="contact">
        <li><span class="contact-label">P :</span> +945-555-0147</li>
        <li><span class="contact-label">E :</span> daniel@brimoutreachpartners.com</li>
        <li><span class="contact-label">A :</span> Marietta, GA based ( Central Time )</li>
      </ul>
      <div class="gavel-art" role="img" aria-label="Large dark gavel and sound block illustration"></div>
      <span class="edge-band"></span>
    </section>
  </main>
</body>
</html>
```